Cutting Edge Ultra High End Investment Company & Business Card

We are an Ultra High End PRIVATE Investment Group that is known for being ULTRA EXCLUSIVE and High NET WORTH. We are kind of the Meridian Vault Onyx for the private investment space in Orange County California, we only invite new investors by referral only.
We are looking for a information only web site that has a big impact once we invite new investors to our site. It needs to be Ultra Modern, Sophisticated, and make an impact. The only contact information that will be listed on the web site is a place where if invite a new investor they can enter a code to unlock access to our members contacts (future page)
We are like the look of a full size web lay out where it has a very large full screen image background.
We are open to any fonts any colors and any designs.
Target Market(s)
Private investors for information only
Industry/Entity Type
Business
Contact Information for Business Card
Please see attached jpeg. this is a very GENERIC
Number of Pages Required
1 page
Requirements
Must have
- Modern, Cutting Edge, Big Impact
Nice to have
- All the info that currently on VR Business Card Attached
Should not have
- Boxing gloves

```html
<!DOCTYPE html>
<html lang="en">
<head>
<meta charset="utf-8">
<title>VR Investment Group</title>
<link href="https://fonts.googleapis.com/css2?family=Open+Sans:wght@300;400;600;700&display=swap" rel="stylesheet">
<style>
:root{
  --ink:#1a1a1a;
  --black:#050505;
  --white:#ffffff;
  --paper:#ffffff;
  --text:#555555;
  --line:#dcdcdc;
  --card-top:#f3f3f3;
  --card-dark:#2c2c2c;
  --footer:#0a0a0a;
}
*{margin:0;padding:0;box-sizing:border-box}
html,body{width:1200px;height:2224px;overflow:hidden}
body{position:relative;background:var(--paper);font-family:"Open Sans",Arial,sans-serif;color:var(--text)}

/* hero */
.hero{position:absolute;left:0;top:0;width:1200px;height:690px;
  background:linear-gradient(160deg,#cfc6b8 0%,#9c8f7e 30%,#3b3e46 60%,#1f232b 100%)}
.topbar{position:absolute;left:0;top:0;width:1200px;height:44px;display:flex;align-items:center;padding:0 90px}
.social{display:flex;gap:10px}
.social span{width:28px;height:28px;border-radius:50%;border:2px solid var(--white)}
.brand-box{position:absolute;left:420px;top:200px;width:360px;height:260px;background:rgba(20,20,22,.6);display:flex;align-items:center;justify-content:center;gap:18px}
.brand-box .mark{width:22px;height:22px;background:var(--white)}
.brand-box .name{font-size:64px;font-weight:300;color:var(--white);letter-spacing:2px;line-height:1}

/* nav */
.main-nav{position:absolute;left:0;top:690px;width:1200px;height:84px;background:var(--black);display:flex;justify-content:center;align-items:stretch}
.main-nav a{display:flex;align-items:center;padding:0 38px;color:var(--white);text-decoration:none;font-size:19px;text-transform:uppercase;letter-spacing:.5px}
.main-nav a.active{background:var(--white);color:var(--ink);margin-top:6px}

/* intro */
.intro{position:absolute;left:90px;top:808px;width:1020px;text-align:center}
.intro h1{font-size:54px;font-weight:300;color:var(--ink);margin-bottom:30px}
.intro p{font-size:15px;line-height:26px;color:var(--text);text-align:justify}

/* service cards */
.service{position:absolute;top:1140px;width:280px;height:440px;border:1px solid var(--line);background:var(--card-top)}
.service h2{padding-top:16px;text-align:center;font-size:22px;font-weight:400;line-height:26px;color:var(--ink);text-transform:uppercase}
.service h2::after{content:"";display:block;width:60px;height:2px;background:var(--ink);margin:8px auto 0}
.service .lower{position:absolute;left:0;top:160px;width:278px;height:279px;background:var(--card-dark);padding:118px 26px 0}
.service .lower p{font-size:13.5px;line-height:20px;text-align:center;color:#e8e8e8}
.service .photo{position:absolute;left:64px;top:96px;width:150px;height:150px;border-radius:50%;border:5px solid var(--white);z-index:2}
.read-more{position:absolute;bottom:18px;right:26px;font-size:12px;font-weight:700;color:var(--white);letter-spacing:.5px}
.read-more::after{content:" \203A"}

/* news band */
.news-band{position:absolute;left:0;top:1660px;width:1200px;height:520px;background:linear-gradient(120deg,#3a3f48 0%,#23262c 55%,#2e3239 100%)}
.band-title{position:absolute;top:44px;font-size:30px;font-weight:400;color:var(--white);text-transform:uppercase}
.news-item{position:absolute;top:110px;width:290px}
.news-item .thumb{width:290px;height:120px;position:relative}
.news-item .date{position:absolute;left:10px;bottom:8px;background:var(--white);color:var(--ink);font-size:10px;padding:2px 6px;font-weight:600}
.news-item h3{font-size:13px;font-weight:600;color:var(--white);margin:16px 0 8px;text-transform:uppercase}
.news-item .meta{font-size:11px;color:#b8b8b8;display:flex;gap:24px;margin-bottom:8px}
.news-item p{font-size:12px;line-height:18px;color:#cfcfcf}
.news-item .btn{display:inline-block;margin-top:24px;background:var(--white);color:var(--ink);font-size:10px;font-weight:700;padding:6px 12px}

.testimonial{position:absolute;left:820px;top:110px;width:300px;text-align:center;color:var(--white)}
.testimonial .avatar{width:100px;height:100px;border-radius:50%;margin:0 auto 8px;border:3px solid var(--white)}
.testimonial .who{font-size:14px;margin-bottom:70px}
.testimonial blockquote{text-align:left;font-size:13.5px;line-height:20px;color:#e0e0e0;padding-left:40px;position:relative}
.testimonial blockquote::before{content:"\201C";position:absolute;left:0;top:-14px;font-size:50px;color:var(--white)}
.arrows{position:absolute;right:80px;top:470px;display:flex;gap:18px}

/* footer */
.site-footer{position:absolute;left:0;top:2180px;width:1200px;height:44px;background:var(--footer);display:flex;justify-content:space-between;align-items:center;padding:0 90px;font-size:11px;color:#cfcfcf}
.site-footer nav{display:flex;gap:48px}
</style>
</head>
<body>

<header class="hero" role="img" aria-label="Photograph of a businessman in a dark suit holding coins in his hands">
  <div class="topbar">
    <div class="social"><span></span><span></span><span></span></div>
  </div>
  <div class="brand-box"><span class="mark"></span><span class="name">VR</span></div>
</header>

<nav class="main-nav">
  <a class="active" href="#">Home</a>
  <a href="#">About Us</a>
  <a href="#">Services</a>
  <a href="#">News</a>
  <a href="#">Contact Us</a>
</nav>

<section class="intro">
  <h1>VR Investment Group</h1>
  <p>We are a private investment group serving a small circle of invited members. Every relationship begins with a referral and grows through patient, disciplined work. Our partners bring decades of experience in capital markets, real estate and private equity, and we hold each portfolio to the same exacting standard we apply to our own. Discretion guides everything we do, from the first conversation to the final report. Members enjoy direct access to senior partners, tailored research and opportunities rarely offered to the wider market. New investors join only by invitation and receive a private code that unlocks our member area, where they can reach the partners directly and follow every holding in full detail.</p>
</section>

<article class="service" style="left:120px">
  <h2>Broker<br>Comparison</h2>
  <div class="photo" role="img" aria-label="Portrait photo of a business advisor" style="background:radial-gradient(circle at 50% 40%,#d9d9d9,#7d8590 70%)"></div>
  <div class="lower"><p>Independent comparison of brokers and custodians, measured on cost, service and security, so every member can choose with full confidence.</p><span class="read-more">READ MORE</span></div>
</article>

<article class="service" style="left:460px">
  <h2>Investment<br>Consulting</h2>
  <div class="photo" role="img" aria-label="Photo of financial charts and paperwork on a desk" style="background:radial-gradient(circle at 50% 45%,#c9d6e4,#5f7a98 75%)"></div>
  <div class="lower"><p>Tailored advice from senior partners who study each goal, weigh every risk and shape a plan that fits your wealth.</p><span class="read-more">READ MORE</span></div>
</article>

<article class="service" style="left:800px">
  <h2>Investment<br>Solutions</h2>
  <div class="photo" role="img" aria-label="Photo of a business meeting at a conference table" style="background:radial-gradient(circle at 50% 45%,#b7b7b7,#3e3e3e 75%)"></div>
  <div class="lower"><p>Private placements, real estate and structured products selected for members and reviewed every quarter with clear, candid reporting.</p><span class="read-more">READ MORE</span></div>
</article>

<section class="news-band" aria-label="Latest news and testimonials">
  <h2 class="band-title" style="left:90px">Latest News</h2>
  <div class="news-item" style="left:90px">
    <div class="thumb" role="img" aria-label="Photo of a city skyline at dusk" style="background:linear-gradient(135deg,#3d6fb3,#b9472e)"><span class="date">18 Jan 2016</span></div>
    <h3>Quarterly outlook for private markets</h3>
    <div class="meta"><span>By admin</span><span>Comments 0</span></div>
    <p>A short look at where our partners see value in the months ahead.</p>
    <span class="btn">READ MORE</span>
  </div>
  <div class="news-item" style="left:420px">
    <div class="thumb" role="img" aria-label="Photo of financial reports and a laptop on a desk" style="background:linear-gradient(135deg,#e9eef3,#8aa3be)"><span class="date">12 Jan 2016</span></div>
    <h3>New members welcomed this season</h3>
    <div class="meta"><span>By admin</span><span>Comments 0</span></div>
    <p>Our circle grows by referral, with new members joining our spring review.</p>
    <span class="btn">READ MORE</span>
  </div>

  <h2 class="band-title" style="left:820px">Testimonials</h2>
  <div class="testimonial">
    <div class="avatar" role="img" aria-label="Portrait photo of a member" style="background:radial-gradient(circle at 50% 40%,#d8b49a,#6b4a3a 75%)"></div>
    <div class="who">Claire Dunmore</div>
    <blockquote>Joining this group changed how I think about wealth. The partners are calm, precise and always one step ahead of the market.</blockquote>
  </div>
  <div class="arrows">
    <svg width="14" height="22" viewBox="0 0 14 22"><path d="M11 2L3 11l8 9" fill="none" stroke="#fff" stroke-width="2.5"/></svg>
    <svg width="14" height="22" viewBox="0 0 14 22"><path d="M3 2l8 9-8 9" fill="none" stroke="#fff" stroke-width="2.5"/></svg>
  </div>
</section>

<footer class="site-footer">
  <span>© All rights reserved, VR Investment, 2015</span>
  <nav><span>Home</span><span>About Us</span><span>News</span><span>Services</span><span>Contact Us</span></nav>
</footer>

</body>
</html>
```